Larkwell Bend responsive web design

We need a responsive, bootstrap compatible (but design only - PSD files) website design for a fly fishing shop and guide service.

Design should be very clean. Home Page design + interior page design please.

Possible Home Page Content:
Slide Show
Highlight Three Features: Guided Trips, Fly Shop, Missouri River
About

Thank you and good luck!

Industry/Entity Type

Shop

Requirements
Must have
• This will be used on Bootstrap CMS so needs 12 column bootstrap measurements.

DESIGN ONLY NEEDED (clean PSD files), no programming required.
Need a Home Page layout and secondary page layout

Must show use of the following:
H1 - H5 font uses
link color
Dropdown for navigation bar
Button example
Should not have
• No cutout images, this will be part of CMS and client needs to be able to update most content without knowing photoshop.

```html
<!DOCTYPE html>
<html lang="en">
<head>
<meta charset="utf-8">
<title>Larkwell Bend</title>
<link rel="stylesheet" href="https://fonts.googleapis.com/css2?family=Roboto:ital,wght@0,300;0,400;0,500;1,400&display=swap">
<style>
:root{
  --sand:#efe4c0;
  --sand-line:#ddd0a8;
  --sky:#7fd0ef;
  --sky-light:#b6e4f6;
  --sky-dark:#4fb3db;
  --ink:#222;
  --text:#555;
  --muted:#777;
  --white:#fff;
  --icon:#888;
  --ring:#eadfbf;
}
*{box-sizing:border-box;margin:0;padding:0}
html,body{width:985px;height:1200px;overflow:hidden}
body{font-family:"Roboto",Arial,sans-serif;color:var(--text);background:var(--white);position:relative}
.topbar{position:absolute;top:0;left:0;width:985px;height:33px;background:var(--sand)}
.topbar .call{position:absolute;right:135px;top:10px;font-size:12.5px;color:var(--muted);display:flex;align-items:center;gap:6px}
.topbar .call b{color:#333;font-weight:500}
.topbar .call svg{width:15px;height:15px}
.login{position:absolute;right:60px;top:5px;width:61px;height:22px;background:var(--sky);color:#244;font-size:10px;font-weight:500;display:flex;align-items:center;justify-content:center}
.navbar{position:absolute;top:33px;left:0;width:985px;height:70px;background:var(--white);box-shadow:0 2px 4px rgba(0,0,0,.15);z-index:2}
.brand{position:absolute;left:61px;top:-20px;width:166px;height:110px;display:flex;align-items:center;gap:8px;z-index:3}
.brand .mark{width:18px;height:18px;background:var(--sky)}
.brand span{font-size:22px;font-weight:500;color:var(--ink)}
.menu{position:absolute;right:60px;top:0;display:flex;height:70px;list-style:none}
.menu li{position:relative;padding:0 12px;font-size:12.5px;line-height:90px;color:#444;text-transform:uppercase}
.menu li.active{background:var(--sky-light);color:#222}
.dropdown{position:absolute;top:70px;left:0;width:167px;height:94px;background:linear-gradient(var(--sky-light),var(--sky));list-style:none;padding:8px 0 0 13px;text-transform:none}
.dropdown li{line-height:20px;font-size:10.5px;font-style:italic;color:#335;padding:0}
.dropdown li::before{content:"›";font-style:normal;margin-right:10px}
.hero{position:absolute;top:103px;left:0;width:985px;height:390px;background:linear-gradient(#b9bfcc 0%,#9c8e78 40%,#a37b5b 72%,#6f6a60 82%,#7a7a5a 100%)}
.hero-title{position:absolute;left:221px;top:174px;width:543px;height:46px;background:rgba(40,40,40,.55);color:#f2e6c4;font-size:37px;font-weight:400;text-align:center;line-height:46px}
.hero-sub{position:absolute;left:256px;top:220px;width:472px;height:48px;background:rgba(40,40,40,.55);color:var(--sky-light);font-size:14px;font-weight:500;text-align:center;padding-top:6px;line-height:18px}
.dots{position:absolute;left:465px;top:360px;display:flex;gap:5px}
.dots i{width:10px;height:10px;border-radius:50%;background:var(--white)}
.dots i:first-child{background:var(--sky)}
.features{position:absolute;top:493px;left:0;width:985px;height:337px;background:radial-gradient(ellipse at 50% 40%,#c4eaf8,var(--sky) 75%);display:flex;padding-left:61px}
.feature{width:271px;margin-right:25px;text-align:center}
.feature .badge{width:144px;height:144px;margin:27px auto 0;border-radius:50%;background:var(--white);border:4px solid var(--ring);display:flex;align-items:center;justify-content:center}
.feature h2{font-size:19px;font-weight:400;color:var(--ink);margin-top:16px;letter-spacing:.3px}
.feature p{font-size:12px;line-height:17px;color:#3d4a55;margin-top:7px;padding:0 8px}
.btn{display:inline-block;width:96px;height:28px;background:var(--sky);border:2px solid var(--sky-dark);color:#223;font-size:12px;line-height:24px;text-align:center}
.feature .btn{margin-top:19px}
.about{position:absolute;top:830px;left:0;width:985px;height:237px}
.about .photo{position:absolute;left:61px;top:32px;width:271px;height:179px;border:3px solid #eee;background:linear-gradient(#8d7b62,#5b6670 55%,#3b3b3b)}
.about h3{position:absolute;left:356px;top:28px;font-size:19px;font-weight:400;color:#333}
.about p{position:absolute;left:356px;top:56px;width:565px;font-size:11px;line-height:18.3px;color:#555}
.about .btn{position:absolute;left:356px;top:184px}
.footer{position:absolute;top:1067px;left:0;width:985px;height:133px;background:var(--sand);border-top:2px solid var(--sand-line)}
.foot-links{position:absolute;left:61px;top:24px;display:flex;gap:21px;font-size:10px;color:#555;list-style:none}
.foot-brand{position:absolute;left:61px;top:70px;font-size:13px;font-weight:500;color:var(--ink)}
.copy{position:absolute;left:167px;top:82px;font-size:9px;line-height:15px;color:#777}
.footer h4{position:absolute;font-size:12.5px;font-weight:400;color:#444;top:22px}
.news{left:582px}.connect{left:808px}
.signup{position:absolute;left:582px;top:47px;width:187px;height:25px;display:flex}
.signup .field{flex:1;background:var(--white);border:1px solid #ccc;font-size:8.5px;font-style:italic;color:#999;padding:7px 9px}
.signup .go{width:24px;background:var(--sky);display:flex;align-items:center;justify-content:center}
.social{position:absolute;left:808px;top:48px;display:flex;gap:6px}
.social i{width:24px;height:24px;border-radius:50%}
</style>
</head>
<body>
<div class="topbar">
  <div class="call"><svg viewBox="0 0 16 16"><rect width="16" height="16" rx="3" fill="#666"/><path d="M5 4c1 0 1.5 2 1 2.5s0 2 2 3.5 2.5 1 3 .5 2 .5 1.5 1.5-2 1.5-4 0-4.5-4-4.5-5.5S4.5 4 5 4z" fill="#efe4c0"/></svg>CALL US: <b>121 555 0147</b></div>
  <div class="login">LOG IN</div>
</div>
<header class="navbar">
  <div class="brand"><i class="mark"></i><span>Larkwell Bend</span></div>
  <ul class="menu">
    <li>Home</li><li>Fly Shop</li>
    <li class="active">Guide Service
      <ul class="dropdown"><li>Dropdown menu 1</li><li>Dropdown menu 2</li><li>Dropdown menu 3</li><li>Dropdown menu 4</li></ul>
    </li>
    <li>Missouri River</li><li>Contact</li>
  </ul>
</header>
<section class="hero" role="img" aria-label="River valley with pine-covered hills and autumn brush along the water">
  <h1 class="hero-title">Welcome to Larkwell Bend</h1>
  <p class="hero-sub">Vivamus egestas risus in magna varius commodo. Sed semper viverra egestas.</p>
  <div class="dots"><i></i><i></i><i></i><i></i></div>
</section>
<section class="features">
  <div class="feature">
    <div class="badge"><svg width="86" height="70" viewBox="0 0 86 70" fill="none" stroke="#888" stroke-width="5"><path d="M43 14C33 8 18 8 8 12v50c10-4 25-4 35 2 10-6 25-6 35-2V12c-10-4-25-4-35 2zM43 14v50"/></svg></div>
    <h2>GUIDED TRIPS</h2>
    <p>Lorem ipsum dolor sit amet, consectetur adipisicing eitseo eiusmod tempor incididunt ut labore et dolore magna aliqua.</p>
    <span class="btn">Learn More</span>
  </div>
  <div class="feature">
    <div class="badge"><div role="img" aria-label="Fly fishing lure illustration" style="width:84px;height:60px;border-radius:40% 50% 30% 50%;background:#8a8a8a"></div></div>
    <h2>FLY SHOP</h2>
    <p>Lorem ipsum dolor sit amet, consectetur adipisicing eitseo eiusmod tempor incididunt ut labore et dolore magna aliqua.</p>
    <span class="btn">Learn More</span>
  </div>
  <div class="feature">
    <div class="badge"><svg width="110" height="60" viewBox="0 0 110 60" fill="none" stroke="#888" stroke-width="4" stroke-linejoin="round"><path d="M2 38L28 4l20 28 14-14 22 22 8-6 16 22"/></svg></div>
    <h2>MISSOURI RIVER</h2>
    <p>Lorem ipsum dolor sit amet, consectetur adipisicing eitseo eiusmod tempor incididunt ut labore et dolore magna aliqua.</p>
    <span class="btn">Learn More</span>
  </div>
</section>
<section class="about">
  <div class="photo" role="img" aria-label="Two anglers in a drift boat on the river"></div>
  <h3>ABOUT US</h3>
  <p>Aliquam molestie, mi et imperdiet euismod, dui purus auctor tellus, et interdum lacus lectus et ante. Sed accumsan sollicitudin sapien, sit amet adipiscing turpis gravida ac. In congue, neque ac lobortis volutpat, libero mauris varius mi, vitae suscipit ipsum ligula vitae risus. Duis aliquam nibh a dui iaculis viverra id a velit. Vivamus egestas risus in magna varius commodo. Sed semper viverra egestas. Etiam pretium porttitor lectus, vel ornare neque porta volutpat. Donec erat purus, faucibus vitae congue vel, porttitor nec lectus. Aenean a nibh eget turpis vehicula tempus ac sed massa.</p>
  <span class="btn">Learn More</span>
</section>
<footer class="footer">
  <ul class="foot-links"><li>Home</li><li>Fly shop</li><li>Guide service</li><li>Missouri river</li><li>Contact</li></ul>
  <div class="foot-brand">Larkwell Bend</div>
  <div class="copy">Copyright © 2014. Larkwell Bend<br>All Right Reserved</div>
  <h4 class="news">Newsletter Sign Up</h4>
  <div class="signup"><div class="field">Enter Email Address</div><div class="go"><svg width="10" height="12" viewBox="0 0 10 12"><path d="M2 1l5 5-5 5" stroke="#fff" stroke-width="2.5" fill="none"/></svg></div></div>
  <h4 class="connect">Connect Us</h4>
  <div class="social"><i style="background:#3b5998"></i><i style="background:#2fa6dc"></i><i style="background:#444"></i><i style="background:#d8262b"></i></div>
</footer>
</body>
</html>
```